Mirela Hartsby ADHD coach needs a flyer

I need a flyer to be sent by email. the copy is attached. It can be changed/reduced to fit the flyer. I would like to keep my website colors. My website is www.mirelahartsby.example - Thank you!

```html
<!DOCTYPE html>
<html lang="en">
<head>
<meta charset="utf-8">
<title>Mirela Hartsby – Academic Success Coaching Flyer</title>
<link rel="stylesheet" href="https://fonts.googleapis.com/css2?family=Barlow+Semi+Condensed:wght@500&family=Jost:wght@300;400;500&display=swap">
<style>
  :root{
    --stage:#3b3b3b;
    --paper:#ffffff;
    --steel:#9bb6c3;
    --ink:#39434a;
    --text:#4a4f52;
    --muted:#7b8286;
    --mist:#e5e8e8;
  }
  *{box-sizing:border-box;margin:0;padding:0}
  html,body{width:1200px;height:1200px;overflow:hidden;background:var(--stage)}
  body{position:relative;font-family:"Jost",sans-serif;color:var(--text)}
  .flyer{
    position:absolute;left:270px;top:133px;width:595px;height:842px;
    background:var(--paper);transform:scale(1.111);transform-origin:0 0;overflow:hidden;
  }
  .abs{position:absolute}
  .line{display:block;white-space:nowrap}
  .hero{left:0;top:0;width:595px;height:420px}
  .hero-title{
    left:37px;top:24px;font-family:"Barlow Semi Condensed",sans-serif;font-weight:500;
    font-size:33px;line-height:38px;color:var(--steel);
  }
  .hero-lead{left:37px;top:228px;font-size:11px;line-height:17px;color:#c9d0d2;font-weight:300}
  .hero-lead strong{color:#fff;font-weight:400;font-size:13.5px}
  .chevrons{left:97px;top:325px}
  .card{border:1px solid var(--steel);background:var(--paper);top:432px;height:255px}
  .card-left{left:36px;width:268px}
  .card-right{left:312px;width:248px}
  .tab{position:absolute;left:0;top:0}
  .tab-title{position:absolute;left:18px;top:4px;font-family:"Barlow Semi Condensed",sans-serif;font-weight:500;font-size:17.5px;color:var(--ink);line-height:20px;white-space:nowrap}
  .tab-sub{position:absolute;left:18px;top:24px;font-size:9px;color:#fff;line-height:11px;white-space:nowrap}
  .card-body{position:absolute;left:18px;right:10px;top:50px}
  .claim{font-size:12.2px;line-height:15px;color:#2f3538;margin-bottom:12px}
  .note{font-size:8.4px;color:var(--muted);font-weight:300;margin-bottom:2px}
  .points{list-style:none}
  .points li{position:relative;padding-left:8px;font-size:8.4px;line-height:11px;color:var(--muted);font-weight:300;margin-bottom:3px}
  .points li::before{content:"";position:absolute;left:0;top:4px;width:3px;height:3px;border-radius:50%;background:var(--text)}
  .card-right .points li{margin-bottom:3px}
  .have{font-size:11px;color:var(--ink);margin:14px 0 14px}
  .band{left:0;top:700px}
  .band-title{left:37px;top:708px;font-family:"Barlow Semi Condensed",sans-serif;font-weight:500;font-size:18.5px;color:var(--ink)}
  .quote{left:37px;width:290px;font-size:6.8px;line-height:9px;color:#4e5659;font-weight:300}
  .arrows{left:265px;top:711px}
  .next-title{left:369px;top:725px;font-family:"Barlow Semi Condensed",sans-serif;font-weight:500;font-size:18.5px;color:var(--ink)}
  .next-body{left:369px;top:753px;width:210px;font-size:10px;line-height:15px;color:var(--ink);font-weight:300}
  .next-body .lead{color:var(--steel);font-weight:400}
  .next-body .contact{font-weight:400;font-size:11px}
</style>
</head>
<body>
<main class="flyer">
  <svg class="abs hero" viewBox="0 0 595 420" width="595" height="420">
    <defs>
      <linearGradient id="sceneTone" x1="0" y1="0" x2="0" y2="1">
        <stop offset="0" stop-color="#5d6465"/>
        <stop offset="1" stop-color="#474d4c"/>
      </linearGradient>
      <linearGradient id="portraitTone" x1="0" y1="0" x2="1" y2="1">
        <stop offset="0" stop-color="#b4c4ca"/>
        <stop offset="0.6" stop-color="#d8d3d3"/>
        <stop offset="1" stop-color="#cfd5d6"/>
      </linearGradient>
    </defs>
    <rect width="595" height="420" fill="url(#sceneTone)" role="img" aria-label="Graduates tossing caps in front of a city skyline, dimmed"/>
    <polygon points="389,0 595,0 595,245 502,420 265,420" fill="url(#portraitTone)" role="img" aria-label="Portrait of the coach standing with arms crossed, wearing a pale pink blazer"/>
  </svg>
  <h1 class="abs hero-title">
    <span class="line">Helping Your Child with</span>
    <span class="line">ADHD or Other</span>
    <span class="line">Learning Challenges</span>
    <span class="line">Thrive in College</span>
    <span class="line">and Beyond</span>
  </h1>
  <p class="abs hero-lead">
    <span class="line"><strong>Academic success coaching</strong> that</span>
    <span class="line">leads to lifelong transformation for</span>
    <span class="line">students with ADHD and similar</span>
    <span class="line">challenges that may have</span>
    <span class="line">impeded their ability to thrive.</span>
  </p>
  <svg class="abs chevrons" width="26" height="84" viewBox="0 0 26 84" aria-hidden="true">
    <g fill="none" stroke="#d7dee0" stroke-width="1.3">
      <polyline points="1,2 13,10 25,2"/><polyline points="1,16 13,24 25,16"/><polyline points="1,30 13,38 25,30"/>
      <polyline points="1,44 13,52 25,44"/><polyline points="1,58 13,66 25,58"/><polyline points="1,72 13,80 25,72"/>
    </g>
  </svg>

  <section class="abs card card-left">
    <svg class="tab" width="172" height="40" aria-hidden="true"><polygon points="0,0 171,0 150,40 0,40" fill="var(--steel)"/></svg>
    <h2 class="tab-title">Empowering Focus:</h2>
    <p class="tab-sub">How Mirela Helps</p>
    <div class="card-body">
      <p class="claim">Mirela has taken students from failing to a 3.0 GPA, and from a C student to the Dean’s List, in just one semester.</p>
      <p class="note">Uniquely positioned to help your child, Mirela:</p>
      <ul class="points">
        <li>Tailors support so that your child improves focus and maximizes their potential in college and beyond.</li>
        <li>Understands your child’s unique needs - she sees the gifts that others often miss.</li>
        <li>Helps with the logistics of scheduling in a way that most advisors can’t, enrolling students in the courses that best suit their learning style.</li>
        <li>Nurtures the brilliance in your bright child.</li>
        <li>Provides a balance between encouraging students and challenging them.</li>
      </ul>
    </div>
  </section>

  <section class="abs card card-right">
    <svg class="tab" width="248" height="40" aria-hidden="true"><polygon points="0,0 245,0 228,40 0,40" fill="var(--steel)"/></svg>
    <h2 class="tab-title" style="left:14px">Realizing Potential:</h2>
    <p class="tab-sub" style="left:14px">The Transformation You’ll See in Your Child</p>
    <div class="card-body" style="left:14px">
      <ul class="points">
        <li>A mindset of self-belief and increased confidence.</li>
        <li>Higher grades and the drive to graduate.</li>
        <li>Social integration and making friends.</li>
        <li>Happiness and fulfillment.</li>
        <li>A deep sense of personal achievement and pride.</li>
      </ul>
      <p class="have">You Will Have:</p>
      <ul class="points">
        <li>Less stress, knowing that your child is in good hands.</li>
        <li>Fewer sleepless nights worrying about your child.</li>
        <li>Confidence that they are receiving the right support.</li>
        <li>Joy and pride at seeing them do well.</li>
      </ul>
    </div>
  </section>

  <svg class="abs band" width="595" height="122" viewBox="0 0 595 122" aria-hidden="true">
    <polygon points="0,0 402,0 337,122 0,122" fill="var(--steel)"/>
    <polygon points="372,18 595,18 595,114 305,114" fill="var(--mist)"/>
  </svg>
  <h2 class="abs band-title">What Parents Say</h2>
  <p class="abs quote" style="top:741px">“Mirela was the glue that kept our daughter in college… as our daughter’s Academic Coach, [she] gave our daughter the ability to finish strong by empowering her with the skills needed to be successful.” —Lorna</p>
  <p class="abs quote" style="top:784px">“Mirela has always told my daughter not that she can succeed, but that she will succeed.” —Petra</p>
  <svg class="abs arrows" width="86" height="28" viewBox="0 0 86 28" aria-hidden="true">
    <g fill="none" stroke="#ffffff" stroke-width="1.3">
      <polyline points="2,2 12,14 2,26"/><polyline points="18,2 28,14 18,26"/><polyline points="34,2 44,14 34,26"/>
      <polyline points="50,2 60,14 50,26"/><polyline points="66,2 76,14 66,26"/>
    </g>
  </svg>
  <h2 class="abs next-title">Next Steps</h2>
  <p class="abs next-body"><span class="lead">To learn more and discuss your child’s individual needs,</span> call <span class="contact">555-014-2368</span> or email <span class="contact">coach@mirelahartsby.example</span></p>
</main>
</body>
</html>
```